Consulting company requires a logo and business card design

I require a logo/business card design for a new company based in Sexsmith Alberta called TallMeadow Field Advisory Ltd. I plan to provide the following services: Construction management/inspection for the oil and gas industry, as well as general consulting for Asset Management, fleet management, etc. Have attached a copy of resume for use as guide for

Target Market(s)

Businesses within the oil and gas production, construction and shipping industry

Industry/Entity Type

Oil And Gas

Contact Information for Business Card

Believe should highlight, services offered, safety, quality,

Logo Text

TallMeadow Field Advisory (TMFA) ?

Font styles to use
Script

Requirements
Must have
• Open to all options

```html
<!DOCTYPE html>
<html lang="en">
<head>
<meta charset="utf-8">
<title>TallMeadow Field Advisory Ltd. – Business Card</title>
<link href="https://fonts.googleapis.com/css2?family=Cinzel:wght@600&family=Open+Sans:wght@400&display=swap" rel="stylesheet">
<style>
  :root {
    --page: #e4e6e8;
    --card: #f8f9fa;
    --navy: #1d3866;
    --ink: #1e1e20;
    --text: #333438;
    --rule: #9a9ca0;
  }
  * { margin: 0; padding: 0; box-sizing: border-box; }
  html, body {
    width: 1200px; height: 970px; overflow: hidden;
    background: var(--page);
  }
  .card {
    position: absolute; left: 100px; top: 206px;
    width: 1000px; height: 557px;
    background: var(--card);
    box-shadow: 0 10px 30px rgba(0,0,0,0.12);
    overflow: hidden;
    font-family: "Open Sans", sans-serif;
    color: var(--text);
  }
  .brand-mark {
    position: absolute; left: 500px; top: 78px;
    width: 110px; height: 110px; border-radius: 50%;
    background: var(--navy);
  }
  .brand-name {
    position: absolute; left: 631px; top: 98px;
    font-family: "Cinzel", serif; font-weight: 600;
    color: var(--navy); line-height: 1;
  }
  .brand-name .main { display: block; font-size: 34px; letter-spacing: 0.5px; }
  .brand-name .sub { display: block; font-size: 17px; margin-top: 8px; letter-spacing: 0.4px; }
  .person-name {
    position: absolute; left: 49px; top: 290px;
    font-family: "Cinzel", serif; font-weight: 600;
    font-size: 30px; color: var(--navy); letter-spacing: 0.5px;
  }
  .person-title {
    position: absolute; left: 49px; top: 327px;
    font-size: 22px;
  }
  .divider {
    position: absolute; left: 49px; top: 374px;
    width: 683px; height: 1px; background: var(--rule);
  }
  .address {
    position: absolute; left: 49px; top: 410px;
    font-size: 22px; line-height: 30px;
  }
  .contacts {
    position: absolute; right: 38px; top: 362px;
    list-style: none; font-size: 21px; line-height: 34.5px;
    text-align: right;
  }
  .contacts li { display: flex; justify-content: flex-end; align-items: center; gap: 10px; }
  .contacts svg { width: 20px; height: 20px; fill: var(--navy); flex: none; }
  .footer-band { position: absolute; left: 0; bottom: 0; width: 1000px; height: 37px; }
</style>
</head>
<body>
<div class="card">
  <div class="brand-mark" aria-hidden="true"></div>
  <div class="brand-name">
    <span class="main">TALLMEADOW</span>
    <span class="sub">FIELD ADVISORY LTD</span>
  </div>

  <div class="person-name">DANIEL OKORO</div>
  <div class="person-title">Managing Director</div>
  <div class="divider"></div>

  <div class="address">
    Suite 4, 118 Prairie Road<br>
    Sexsmith, Alberta
  </div>

  <ul class="contacts">
    <li>+ 000 000 0000
      <svg viewBox="0 0 20 20"><path d="M6 1h8a1 1 0 0 1 1 1v16a1 1 0 0 1-1 1H6a1 1 0 0 1-1-1V2a1 1 0 0 1 1-1zm1 2v11h6V3zm3 12.5a1 1 0 1 0 0 2 1 1 0 0 0 0-2z"/></svg>
    </li>
    <li>+ 000 000 0000
      <svg viewBox="0 0 20 20"><path d="M2 7c0-2 3-4 8-4s8 2 8 4v1.5h-4V7H6v1.5H2zm4 3h8l3 6H3z"/></svg>
    </li>
    <li>info@tallmeadowfa.com
      <svg viewBox="0 0 20 20"><path d="M1 4h18v12H1zm2 2v.4l7 5 7-5V6l-7 5z"/></svg>
    </li>
    <li>www.tallmeadowfa.com
      <svg viewBox="0 0 20 20"><circle cx="10" cy="10" r="8.5" fill="none" stroke="#1d3866" stroke-width="2"/><path d="M1.5 10h17M10 1.5c-4 4-4 13 0 17M10 1.5c4 4 4 13 0 17" fill="none" stroke="#1d3866" stroke-width="1.6"/></svg>
    </li>
  </ul>

  <svg class="footer-band" viewBox="0 0 1000 37" preserveAspectRatio="none" aria-hidden="true">
    <polygon points="0,16 495,16 478,37 0,37" fill="var(--navy)"/>
    <polygon points="490,37 505,19 525,19 510,37" fill="#c9ccd1"/>
    <polygon points="540,0 1000,0 1000,37 505,37" fill="var(--ink)"/>
  </svg>
</div>
</body>
</html>
```